Illustrate a statistic and its significance

Please create a graphical representation of the success rate of the Lanton Procedure for our website. The Lanton Procedure has a success rate of 80%. This means the procedure is successful for 8 out of every 10 people. An 80% success rate by itself is great. However, it's even more impressive when you consider that the only people we perform this procedure on are patients who have exhausted conventional treatment options for migraines and headaches. I would really like to emphasize both the success rate and the type of patients we are successful in treating with this procedure.
For example, you could create an illustration of outlines of 10 people with 8 of them shaded in, which would represent an 80% success rate. Then, underneath this image, you could add a bullet list of the types of treatments patients (such as the 10 figures in the image) have tried before coming to us/having this procedure, which include the following:
Prescription medications
Trigger point injections
Nerve blocks
Migraine surgery
Velquin
Chiropractic care
Physical therapy
Biofeedback
Massage
Acupuncture
Or maybe there is another/better way to represent this statistic graphically? I'm just looking for an effective illustration of this important statistic and its significance.
Our brand colors are red (#fd444a) and blue (#214170)
Thank you!
Target Market(s)
People who suffer from chronic migraines and headaches
Industry/Entity Type
Healthcare/Medical
Other font styles liked:
- Athiti

```html
<!DOCTYPE html>
<html lang="en">
<head>
<meta charset="utf-8">
<title>Lanton Procedure – Success Rate</title>
<link href="https://fonts.googleapis.com/css2?family=Ubuntu:wght@300;400;500;700&family=Oswald:wght@700&display=swap" rel="stylesheet">
<style>
  :root {
    --frame: #575556;
    --card: #efefef;
    --red: #e8464f;
    --blue: #173f70;
    --muted: #c9c7d3;
    --ink: #222222;
    --white: #ffffff;
  }
  * { margin: 0; padding: 0; box-sizing: border-box; }
  html, body {
    width: 1200px; height: 753px; overflow: hidden;
    background: var(--frame);
    font-family: "Ubuntu", sans-serif;
  }
  .card {
    position: absolute; left: 51px; top: 78px;
    width: 1098px; height: 597px;
    background: var(--card);
    overflow: hidden;
  }
  .kicker {
    position: absolute; left: 81px; top: 46px;
    font-weight: 300; font-size: 23px; letter-spacing: 1.2px;
    color: var(--blue); white-space: nowrap;
  }
  .headline {
    position: absolute; left: 80px; top: 78px;
    font-weight: 700; font-size: 42px; letter-spacing: 1.6px;
    color: var(--red); white-space: nowrap;
  }
  .people {
    position: absolute; left: 81px; top: 162px;
    display: grid; grid-template-columns: repeat(5, 50px);
    column-gap: 15px; row-gap: 11px;
  }
  .person { width: 50px; height: 110px; display: block; }
  .person--filled { fill: var(--blue); }
  .person--empty { fill: var(--muted); }
  .stat-intro {
    position: absolute; left: 425px; top: 172px;
    font-size: 14px; letter-spacing: 0.6px;
    color: var(--blue); white-space: nowrap;
  }
  .stat-number {
    position: absolute; left: 418px; top: 168px;
    font-family: "Oswald", sans-serif; font-weight: 700;
    font-size: 188px; line-height: 1; letter-spacing: -4px;
    color: var(--red);
  }
  .stat-percent {
    position: absolute; left: 578px; top: 233px;
    width: 26px; height: 28px; background: var(--card);
    color: var(--red); font-weight: 700; font-size: 20px;
    line-height: 28px; text-align: center;
  }
  .stat-ribbon {
    position: absolute; left: 425px; top: 347px;
    width: 170px; height: 40px;
  }
  .stat-ribbon svg { position: absolute; inset: 0; }
  .stat-ribbon span {
    position: absolute; inset: 0;
    display: flex; align-items: center; justify-content: center;
    color: var(--white); font-weight: 500; font-size: 21px; letter-spacing: 0.8px;
  }
  .services-title {
    position: absolute; left: 80px; top: 424px;
    font-weight: 500; font-size: 20px; letter-spacing: 0.8px;
    color: var(--red);
  }
  .services-rule {
    position: absolute; left: 82px; top: 450px;
    width: 133px; height: 1.5px; background: var(--blue);
  }
  .services-list {
    position: absolute; top: 465px; list-style: none;
    font-size: 14px; line-height: 18.4px; letter-spacing: 0.5px;
    color: var(--ink);
  }
  .services-list li::before { content: "•"; margin-right: 5px; }
  .services-list--left { left: 82px; }
  .services-list--right { left: 290px; }
  .portrait {
    position: absolute; left: 660px; top: 24px;
    width: 420px; height: 573px;
    border-radius: 190px 190px 0 0;
    background:
      radial-gradient(circle at 38% 22%, rgba(232,70,79,0.35), rgba(232,70,79,0) 22%),
      linear-gradient(180deg, #8a8a8a 0%, #5f5f5f 45%, #4c4c4c 100%);
  }
</style>
</head>
<body>
<svg width="0" height="0" style="position:absolute">
  <symbol id="figure" viewBox="0 0 92 202">
    <circle cx="46" cy="22" r="22"/>
    <rect x="0" y="52" width="92" height="22" rx="10"/>
    <rect x="0" y="56" width="17" height="72" rx="8"/>
    <rect x="75" y="56" width="17" height="72" rx="8"/>
    <rect x="21" y="52" width="50" height="78"/>
    <rect x="21" y="110" width="23" height="92" rx="10"/>
    <rect x="48" y="110" width="23" height="92" rx="10"/>
  </symbol>
</svg>

<main class="card">
  <p class="kicker">Exhausted with conventional treatment for</p>
  <h1 class="headline">Migraines and Headaches?</h1>

  <div class="people" aria-label="8 of 10 patients helped">
    <svg class="person person--filled"><use href="#figure"/></svg>
    <svg class="person person--filled"><use href="#figure"/></svg>
    <svg class="person person--filled"><use href="#figure"/></svg>
    <svg class="person person--filled"><use href="#figure"/></svg>
    <svg class="person person--filled"><use href="#figure"/></svg>
    <svg class="person person--filled"><use href="#figure"/></svg>
    <svg class="person person--filled"><use href="#figure"/></svg>
    <svg class="person person--filled"><use href="#figure"/></svg>
    <svg class="person person--empty"><use href="#figure"/></svg>
    <svg class="person person--empty"><use href="#figure"/></svg>
  </div>

  <p class="stat-intro">We offer a procedure of</p>
  <div class="stat-number">80</div>
  <div class="stat-percent">%</div>
  <div class="stat-ribbon">
    <svg viewBox="0 0 170 40" width="170" height="40" preserveAspectRatio="none">
      <polygon points="0,0 170,0 165,20 170,40 0,40 5,20" fill="var(--red)"/>
    </svg>
    <span>success rate</span>
  </div>

  <h2 class="services-title">Our Services</h2>
  <div class="services-rule"></div>
  <ul class="services-list services-list--left">
    <li>Prescription medications</li>
    <li>Trigger point injections</li>
    <li>Nerve blocks</li>
    <li>Migraine surgery</li>
    <li>Velquin</li>
  </ul>
  <ul class="services-list services-list--right">
    <li>Chiropractic care</li>
    <li>Physical therapy</li>
    <li>Biofeedback</li>
    <li>Massage</li>
    <li>Acupuncture</li>
  </ul>

  <div class="portrait" role="img" aria-label="Black and white photo of a woman holding her temple in pain, with a red glow marking the headache"></div>
</main>
</body>
</html>
```